43 Year Old Construction firm needs Updated Business Card & Stationery Design

We are an established and well known (in our market) commercial construction firm. We need a cleaner and more modern look for our corporate identity material. We would like to continue to use our current colors and logo.
We are thinking about incorporating a slogan on our business card (either front or back): "Striving to be the most trusted builder in our market." The text could change at some point. Our website is www.kradworth.example . Sample card is attached. Some will have more phone numbers, etc...
Updates

Target Market(s)

Commercial and institutional clients.

Industry/Entity Type

Construction Company

Contact Information for Business Card

See attached for existing card. But don't be constrained.

Requirements
Must have
• Logo, name, title, address, website, email, phone numbers (as few as one, as many as three)
• Slogan on front or back "Striving to be the most trusted builder in our market"
• Use existing logo and colors

```html
<!DOCTYPE html>
<html lang="en">
<head>
<meta charset="utf-8">
<title>Kradworth Constructors – Business Card</title>
<link href="https://fonts.googleapis.com/css2?family=Source+Sans+3:wght@400;600;700&display=swap" rel="stylesheet">
<style>
  :root {
    --backdrop: #3a3330;
    --card: #141414;
    --card-edge: #1e1e1e;
    --brand-blue: #1f5fae;
    --brand-green: #2e9b4c;
    --text-light: #d9d9d9;
    --silver: #cfcfcf;
    --divider: #5a5a5a;
  }
  * { margin: 0; padding: 0; box-sizing: border-box; }
  html, body { width: 1200px; height: 814px; overflow: hidden; }
  body {
    background: var(--backdrop);
    font-family: "Source Sans 3", "Myriad Pro", sans-serif;
    display: flex;
    align-items: center;
    justify-content: center;
    gap: 44px;
  }
  .card {
    width: 540px;
    height: 309px;
    background: var(--card);
    border: 1px solid var(--card-edge);
    position: relative;
    box-shadow: 0 10px 30px rgba(0,0,0,.45);
  }

  /* Front: contact side */
  .card-front { display: flex; align-items: center; }
  .brand-block {
    width: 250px;
    display: flex;
    align-items: center;
    justify-content: center;
    gap: 10px;
    padding-left: 24px;
  }
  .brand-square {
    width: 22px; height: 22px;
    background: var(--brand-blue);
    flex: none;
  }
  .brand-name {
    color: var(--text-light);
    font-weight: 700;
    font-size: 19px;
    line-height: 1.1;
    letter-spacing: .04em;
    text-transform: uppercase;
  }
  .divider {
    width: 1px; height: 150px;
    background: linear-gradient(to bottom, transparent, var(--divider), transparent);
    margin: 0 22px;
  }
  .contact { color: var(--text-light); font-size: 14px; line-height: 1.45; }
  .person-name { color: var(--brand-blue); font-size: 17px; font-weight: 600; line-height: 1.1; }
  .person-title { color: var(--brand-green); font-size: 14px; margin-bottom: 8px; }
  .contact-line { display: flex; align-items: center; gap: 8px; }
  .contact-line svg { width: 12px; height: 12px; flex: none; }

  /* Back: brand side */
  .card-back {
    display: flex;
    flex-direction: column;
    align-items: center;
    justify-content: center;
    gap: 34px;
  }
  .back-brand {
    color: var(--silver);
    font-weight: 700;
    font-size: 34px;
    letter-spacing: .05em;
    text-transform: uppercase;
  }
  .slogan { color: var(--text-light); font-size: 12.5px; letter-spacing: .02em; }
</style>
</head>
<body>
  <section class="card card-front">
    <div class="brand-block">
      <span class="brand-square"></span>
      <span class="brand-name">Kradworth<br>Constructors</span>
    </div>
    <div class="divider"></div>
    <div class="contact">
      <p class="person-name">Daniel Marsh</p>
      <p class="person-title">CEO/Founder</p>
      <p>4120 harbor lane</p>
      <p>fairview, MO 63000</p>
      <p class="contact-line">
        <svg viewBox="0 0 12 12"><circle cx="6" cy="6" r="6" fill="var(--brand-blue)"/><path d="M4 3l1.2 1.4-.6.8a4 4 0 0 0 2.2 2.2l.8-.6L9 8l-.7.9C6 9 3 6 3.1 3.7z" fill="#141414"/></svg>
        555.014.2290
      </p>
      <p class="contact-line">
        <svg viewBox="0 0 12 12"><circle cx="6" cy="6" r="6" fill="var(--brand-blue)"/><rect x="3" y="4" width="6" height="4.2" fill="#141414"/><path d="M3 4l3 2.3L9 4" stroke="var(--brand-blue)" stroke-width=".8" fill="none"/></svg>
        name@kradworth.example
      </p>
      <p class="contact-line">
        <svg viewBox="0 0 12 12"><circle cx="6" cy="6" r="6" fill="var(--brand-blue)"/><circle cx="6" cy="6" r="3.2" fill="none" stroke="#141414" stroke-width=".9"/><path d="M2.8 6h6.4M6 2.8v6.4" stroke="#141414" stroke-width=".8"/></svg>
        www.kradworth.example
      </p>
    </div>
  </section>

  <section class="card card-back">
    <p class="back-brand">Kradworth Constructors</p>
    <p class="slogan">Striving to be the most trusted builder in our market.</p>
  </section>
</body>
</html>
```